Brintell's Business Card

I need some designs for a new business card including the new logo attached. An old example of our business card is also attached to show all the data that should be included on the new design.
**I added some more examples someone had mocked up**

Contact Information for Business Card

Should include all info on other examples uploaded.

```html
<!DOCTYPE html>
<html lang="en">
<head>
<meta charset="utf-8">
<title>Brintell's Business Card</title>
<link rel="stylesheet" href="https://fonts.googleapis.com/css2?family=Montserrat:wght@700&family=PT+Sans:wght@400;700&display=swap">
<style>
  :root {
    --brand-blue: #1170c0;
    --brand-red: #ec2129;
    --ink: #1c1c1c;
    --paper: #ffffff;
    --stage-dark: #000000;
    --stage-mid: #2a2a2a;
  }
  * { box-sizing: border-box; margin: 0; padding: 0; }
  html, body { width: 1200px; height: 960px; overflow: hidden; }
  body {
    position: relative;
    background: radial-gradient(ellipse at 50% 50%, var(--stage-mid) 0%, #121212 55%, var(--stage-dark) 100%);
    font-family: "PT Sans", sans-serif;
  }
  .card {
    position: absolute;
    width: 746px;
    height: 426px;
    background: var(--paper);
    overflow: hidden;
  }
  .card--front { left: 160px; top: 52px; }
  .card--back { left: 280px; top: 504px; }

  .brand {
    position: absolute;
    display: flex;
    align-items: center;
    gap: 16px;
  }
  .brand-dot {
    border-radius: 50%;
    background: var(--brand-red);
    flex: none;
  }
  .brand-name {
    font-family: "Montserrat", sans-serif;
    font-weight: 700;
    color: var(--brand-blue);
    line-height: 1;
    letter-spacing: 0.5px;
  }
  .card--front .brand { left: 40px; top: 60px; }
  .card--front .brand-dot { width: 84px; height: 84px; }
  .card--front .brand-name { font-size: 54px; }
  .card--back .brand { left: 120px; top: 146px; }
  .card--back .brand-dot { width: 104px; height: 104px; }
  .card--back .brand-name { font-size: 66px; }

  .band-tab {
    position: absolute;
    left: 0;
    background: var(--brand-red);
    color: var(--paper);
    display: flex;
    align-items: center;
  }
  .band-line {
    position: absolute;
    left: 0;
    width: 100%;
    background: var(--brand-red);
  }
  .card--front .band-tab {
    top: 283px; width: 277px; height: 47px;
    clip-path: polygon(0 0, 264px 0, 277px 100%, 0 100%);
    padding-left: 38px;
    font-weight: 700; font-size: 26px;
  }
  .card--front .band-line { top: 316px; height: 14px; }
  .card--back .band-tab {
    top: 321px; width: 420px; height: 46px;
    clip-path: polygon(0 0, 406px 0, 420px 100%, 0 100%);
    padding-left: 34px;
    font-size: 21px;
  }
  .card--back .band-line { top: 354px; height: 13px; }

  .contact-list {
    position: absolute;
    left: 38px; top: 336px;
    list-style: none;
    font-size: 20px;
    color: var(--ink);
  }
  .contact-item {
    display: flex;
    align-items: center;
    gap: 14px;
    height: 31px;
    letter-spacing: 0.3px;
  }
  .contact-icon { width: 20px; height: 20px; fill: var(--brand-blue); flex: none; }

  .credentials {
    position: absolute;
    right: 31px; top: 334px;
    text-align: right;
    font-size: 20px;
    color: var(--ink);
    line-height: 32px;
  }
  .call-to-action {
    position: absolute;
    left: 0; width: 100%; top: 376px;
    text-align: center;
    font-size: 20px;
    color: var(--ink);
  }
</style>
</head>
<body>
  <section class="card card--front" aria-label="Business card front">
    <div class="brand">
      <span class="brand-dot"></span>
      <span class="brand-name">BRINTELL'S</span>
    </div>
    <div class="band-line"></div>
    <div class="band-tab">Dale Brintell</div>
    <ul class="contact-list">
      <li class="contact-item">
        <svg class="contact-icon" viewBox="0 0 24 24" aria-hidden="true"><path d="M6.6 10.8a15.2 15.2 0 0 0 6.6 6.6l2.2-2.2c.3-.3.7-.4 1-.2 1.1.4 2.3.6 3.6.6.6 0 1 .4 1 1V20c0 .6-.4 1-1 1C10.6 21 3 13.4 3 4c0-.6.4-1 1-1h3.5c.6 0 1 .4 1 1 0 1.3.2 2.5.6 3.6.1.3 0 .7-.2 1z"/></svg>
        555.014.2286
      </li>
      <li class="contact-item">
        <svg class="contact-icon" viewBox="0 0 24 24" aria-hidden="true"><path d="M12 2 2 9v12h20V9zm0 2.4 7.6 5.3L12 14 4.4 9.7z"/></svg>
        hvacbrintell@mailbox.com
      </li>
    </ul>
    <div class="credentials">
      <p>LICENSED &amp; INSURED</p>
      <p>FAMILY OWNED &amp; OPERATED</p>
    </div>
  </section>

  <section class="card card--back" aria-label="Business card back">
    <div class="brand">
      <span class="brand-dot"></span>
      <span class="brand-name">BRINTELL'S</span>
    </div>
    <div class="band-line"></div>
    <div class="band-tab">Serves Maple Falls, IA &amp; Surrounding Areas</div>
    <p class="call-to-action">CALL TODAY FOR ALL YOUR HVAC, REFRIGERATION &amp; PLUMBING NEEDS</p>
  </section>
</body>
</html>
```